BKA

Please send us some options for letterhead I attached our Logo. In addition to the Logo we need this information somewhere on the page

47 Fenbury Lane
Marlow Falls, ST 00417
555-481-7629

```html
<!DOCTYPE html>
<html lang="en">
<head>
<meta charset="utf-8">
<title>BKA Letterhead</title>
<link rel="stylesheet" href="https://fonts.googleapis.com/css2?family=Open+Sans:wght@400;600&display=swap">
<style>
  :root {
    --backdrop: #46474c;
    --paper: #ffffff;
    --brand-blue: #0b6fb8;
    --brand-dark: #3a3434;
    --footer-text: #ffffff;
  }
  * { margin: 0; padding: 0; box-sizing: border-box; }
  html, body {
    width: 1200px;
    height: 935px;
    overflow: hidden;
    background: var(--backdrop);
    font-family: "Open Sans", Arial, sans-serif;
  }
  .letterhead {
    position: absolute;
    left: 300px;
    top: 80px;
    width: 600px;
    height: 776px;
    background: var(--paper);
    box-shadow: 0 10px 30px rgba(0, 0, 0, 0.35);
  }
  .brand {
    position: absolute;
    left: 44px;
    top: 40px;
    display: flex;
    align-items: center;
    gap: 8px;
  }
  .brand-square {
    width: 22px;
    height: 22px;
    background: var(--brand-blue);
  }
  .brand-name {
    font-size: 22px;
    font-weight: 600;
    letter-spacing: 1px;
    color: var(--brand-dark);
    line-height: 1;
  }
  .footer-band {
    position: absolute;
    left: 0;
    bottom: 0;
    width: 100%;
    height: 34px;
    background: var(--brand-blue);
    display: flex;
    align-items: center;
    justify-content: flex-end;
    padding-right: 40px;
  }
  .footer-contact {
    font-size: 13px;
    font-weight: 400;
    color: var(--footer-text);
    letter-spacing: 0.2px;
    white-space: nowrap;
  }
</style>
</head>
<body>
  <main class="letterhead">
    <header class="brand">
      <span class="brand-square"></span>
      <span class="brand-name">BKA</span>
    </header>
    <footer class="footer-band">
      <p class="footer-contact">47 Fenbury Lane Marlow Falls, ST 00417, 555-481-7629</p>
    </footer>
  </main>
</body>
</html>
```